Honey packaging lable for small honey producer

We are small scale bee keepers and need a design for labels for our honey.
We curently sell honey in 2 different package sizes, 500gm and 1kg so the label would need to be suitable for both.
The plan is to print the label on brown or "craft" paper with a laser printer to give a rustic feel so the design will need to be monotone.
As we are in Australia all measurements will need to be metric
Label dimensions should be 105mm wide by 59.4mm high (so we can fit 10 labels per sheet of a4 paper).
The batch number, nett weight and number of servings per package on the nutritional label need to be able to be changed to suit the packaging size.
Designs need to be able to be opened and printed from open source software such as Free Desk, Pixo or similar. If proprietary software is used there must be at least a free program to allow printing and basic manipulation of the design.
Updates

Thank you everyone for the designs you submitted. I have been surprised by the quality of work supplied and wish I had the budget to make a payment to everyone, but unfortunately that is not the case :( 

This is my first time doing anything like this and it has been an interesting experience. I have definitely learned lots and hopefully I will be a better and more concise brief writer next time :)

The only other feedback I would like to give is to read the brief carefully. There were some designers that submited color designs which weren't suitable for my needs which may have been avoided.

Thank you again for all your hard work.

All the best.

Derek & Margot.

Industry/Entity Type

Printer

Requirements
Must have
• Brindlecote Farm
honey
Nett Weight
Batch Number:
Produced by: Derek and Margot Tollingham, Marbury Flat, Victoria. 0429 163072

Nutritional panel similar to : http://www.quillorbe.net.au/images/products/jars-pails-L030.jpg
Nice to have
• Produced in the Brannocks
Pure, Natural, raw.
Contains traces of pollen and wax
Honey is a natural product and may crystallize. It may be eaten as is or re-liquefied by placing the container in hot water.
Should not have
• No twee cartoon bees or skep bee hives please!

```html
<!DOCTYPE html>
<html lang="en">
<head>
<meta charset="utf-8">
<title>Brindlecote Farm Honey Label</title>
<link rel="stylesheet" href="https://fonts.googleapis.com/css2?family=Arimo:wght@400;700&family=Homemade+Apple&display=swap">
<style>
  :root {
    --backdrop-top: #6cc3d3;
    --backdrop-bottom: #eef7fa;
    --kraft: #d0976a;
    --ink: #2c1e18;
    --ink-soft: #3b2a22;
  }
  * { box-sizing: border-box; margin: 0; padding: 0; }
  html, body { width: 1200px; height: 1000px; overflow: hidden; }
  body {
    background: linear-gradient(to bottom, var(--backdrop-top), var(--backdrop-bottom));
    font-family: "Arimo", Arial, sans-serif;
    color: var(--ink);
  }
  .label {
    position: absolute;
    left: 162px; top: 253px;
    width: 876px; height: 494px;
    background: var(--kraft);
    border: 1.5px solid var(--ink-soft);
  }
  .label > * { position: absolute; }
  .label-text { font-size: 14px; line-height: 20px; }
  .origin { left: 23px; top: 36px; }
  .nutrition-title { left: 23px; top: 76px; }
  .servings { left: 23px; top: 116px; }

  .nutrition-heads {
    left: 95px; top: 186px; width: 105px;
    display: flex; font-size: 10.5px;
  }
  .nutrition-heads span { flex: 1; text-align: center; }
  .nutrition-table {
    left: 23px; top: 210px; width: 177px; height: 205px;
    border-collapse: collapse; border: 1px solid var(--ink);
    font-size: 9.5px;
  }
  .nutrition-table th, .nutrition-table td { padding: 0 4px; }
  .nutrition-table th { font-weight: 400; height: 27px; border-bottom: 1px solid var(--ink); }
  .nutrition-table td { height: 23px; }
  .nutrition-table tr.spacer td { height: 8px; }
  .nutrition-table .col-value { text-align: right; border-left: 1px solid var(--ink); }
  .nutrition-table th.col-value { text-align: center; }
  .nutrition-table th:first-child { border-right: 0; }

  .emblem { left: 235px; top: 15px; }

  .producer { left: 675px; top: 36px; }
  .producer .farm-name { font-weight: 700; }
  .producer p + p { margin-top: 20px; }

  .care-note {
    left: 673px; top: 262px; width: 185px;
    font-family: "Homemade Apple", cursive;
    font-size: 11.5px; line-height: 26px;
    text-align: justify;
  }
  .weight-badge { left: 590px; top: 396px; }
  .nett-weight { left: 585px; top: 464px; font-size: 14px; }
</style>
</head>
<body>
  <main class="label">
    <p class="label-text origin">Product of Australia</p>
    <p class="label-text nutrition-title">Nutritional information 500 g</p>
    <p class="label-text servings">Serving per package 33<br>Serving Size 15 g</p>

    <div class="nutrition-heads"><span>Quantity</span><span>Quantity</span></div>
    <table class="nutrition-table">
      <tr><th></th><th class="col-value">Per serving</th><th class="col-value">per 100 g</th></tr>
      <tr class="spacer"><td></td><td class="col-value"></td><td class="col-value"></td></tr>
      <tr><td>Energy</td><td class="col-value">214KJ</td><td class="col-value">1416 KJ</td></tr>
      <tr><td>Protein</td><td class="col-value">.05 g</td><td class="col-value">.03 g</td></tr>
      <tr><td>Fat-Total</td><td class="col-value">0 g</td><td class="col-value">0 g</td></tr>
      <tr><td>Saturated</td><td class="col-value">0 g</td><td class="col-value">0 g</td></tr>
      <tr><td>Carbohydrales</td><td class="col-value">12.5 g</td><td class="col-value">83.1 g</td></tr>
      <tr><td>Sugers</td><td class="col-value">12.5 g</td><td class="col-value">82.5 g</td></tr>
      <tr><td>Sodium</td><td class="col-value">2.3 mg</td><td class="col-value">15 mg</td></tr>
      <tr class="spacer"><td></td><td class="col-value"></td><td class="col-value"></td></tr>
    </table>

    <svg class="emblem" width="412" height="412" viewBox="0 0 412 412" role="img"
         aria-label="Round honey emblem: hand-lettered 'Honey' with dripping honey over honeycomb and a bee, ringed by 'Pure • Natural • Raw'">
      <circle cx="206" cy="206" r="204" fill="var(--ink)"/>
    </svg>

    <div class="label-text producer">
      <p class="farm-name">Brindlecote Farm<br>Produced in the Brannocks</p>
      <p>Batch Number:</p>
      <p>Produced by:<br>Derek and Margot Tollingham,<br>Marbury Flat,<br>Victoria. 0429 163072</p>
    </div>

    <p class="care-note">Honey is a natural product and may crystallize. It may be eaten as is or re-liquefied by placing the container in hot water.</p>

    <svg class="weight-badge" width="66" height="70" viewBox="0 0 66 70">
      <polygon points="33,3 62,19 62,51 33,67 4,51 4,19" fill="none" stroke="var(--ink)" stroke-width="2.5"/>
      <text x="29" y="47" text-anchor="middle" font-family="Arimo, Arial, sans-serif" font-weight="700" font-size="28" fill="var(--ink)">1</text>
      <text x="46" y="47" text-anchor="middle" font-family="Arimo, Arial, sans-serif" font-size="13" fill="var(--ink)">kg</text>
    </svg>
    <p class="nett-weight">Nett Weight</p>
  </main>
</body>
</html>
```